More Modern Look Required! Industry leading Property Management company needs a new website!

We are wanting to make our website more modern, as we find it is too cluttered, seems "old" and we want a new look. (www.tallowbrookrm.com)

We are wanting something fresh, clean and responsive, something that aligns with today's social media demands, something that allows our potential customers to immediately get a sense of the type of company we are.

Our current website was created on Wordpress and we will be keeping that core platform but wanting a new look and feel to it. The only thing we want to keep on the website is our "FOR RENT" page, although again we are open to having that look completely different as well (our programmers can adapt the functionality later)

Here is a synopsis of our branding statements:

CORE VALUES:
1. Passion
2. Innovation
3. Integrity (doing the right thing, even when it's difficult)
4. Empathy
5. Education

CORE FOCUS:
Our vision is to be the premier company for the delivery of all aspects of property management showing our passion for this industry, by innovating our service using cutting-edge technology, helping and educating investors to create aspirational and sustainable communities, adding value to their real estate assets, and working in partnership with all stakeholders including residents, showing empathy and integrity.

Brand Essence

When our customers experience our product or service, it brings forth an emotion of absolute trust that we have their best interests at heart

Brand Personality

We are a company that is passionate about our customers, our company and our vision to be leaders in the field of property management. We are visionaries that aren't afraid to use cutting edge technologies to improve our products and service.

Position or Value Proposition

To whom are we speaking?
- real estate investors, including first timers that are giving us their first starter home. They are not "big time" investors, and because they are giving us their first home (in contrast to an investor buying a rental property, often sight unseen) they are more emotionally tied to their property and will require a company that inspires trust and confidence.

What is our brand promise?
- we will do our best to serve our clients, both owners and tenants, to give them prompt communication, clear, concise answers to their questions, and look after their property quickly and competently.

Why is our product different than the competition and why should our customers care?
- Our management product is superior because we use a combination of technology and strict procedures to ensure each client's experience is consistent, each and every time.
Updates

Need extra days to review

Industry/Entity Type

Real Estate and Property Management

Number of Pages Required

5+ page

Requirements
Must have
• Must be compatible on Wordpress, our existing web platform. Please see our existing website at www.tallowbrookrm.com to familiarize yourself with our current site. Must incorporate For Rent section
Nice to have
• Built in reviews, contact us form, awards page including Fernleigh Patron Prizes (we just won again for Best Property Management Company, 8 years in a row)
Should not have
• Too many pages. Currently we feel there is too much information on each tab, and we can consolidate into about 5 or 6 tabs.

```html
<!DOCTYPE html>
<html lang="en">
<head>
<meta charset="utf-8">
<title>Tallowbrook Residential Management</title>
<link href="https://fonts.googleapis.com/css2?family=Poppins:wght@400;500;600;700&display=swap" rel="stylesheet">
<style>
:root{
  --navy:#1b2538;
  --navy-deep:#1a2336;
  --accent:#f39a1e;
  --teal-a:#1f9ccb;
  --teal-b:#176a8c;
  --brand-blue:#2a5298;
  --ink:#1d2433;
  --body:#3b3f48;
  --muted:#f8f8f8;
  --pale-blue:#dde8fc;
  --white:#ffffff;
  --line:#dcdcdc;
}
*{box-sizing:border-box;margin:0;padding:0}
html,body{width:1200px;height:3307px;overflow:hidden}
body{font-family:'Poppins',sans-serif;color:var(--ink);background:var(--white);position:relative}
.abs{position:absolute}

/* hero */
.hero{left:0;top:0;width:1200px;height:583px;
  background:radial-gradient(ellipse at 55% 60%,#6b6f66 0%,#4d5a44 35%,#2f3a2c 70%,#26302a 100%)}
.hero-shade{left:0;top:0;width:1200px;height:583px;background:rgba(15,20,25,.38)}
.logo{left:68px;top:36px;display:flex;align-items:center;gap:8px;color:var(--white);font-weight:600;font-size:17px;letter-spacing:.5px}
.logo-mark{width:24px;height:24px;background:var(--teal-a);border-radius:3px}
.nav{top:41px;font-size:13px;color:#e6e9ee;letter-spacing:.3px}
.nav.active{font-weight:500;color:var(--white)}
.hero-title{left:60px;width:1080px;top:132px;text-align:center;color:var(--white);font-weight:600;font-size:43px;line-height:60px}
.hero-sub{left:60px;width:1080px;top:324px;text-align:center;color:#f1f1f1;font-size:17.5px;line-height:25px}
.hero-btn{left:534px;top:402px;width:132px;height:43px;border:1px solid #fff;border-radius:22px;color:#fff;font-size:12.5px;font-weight:600;display:flex;align-items:center;justify-content:center;letter-spacing:.3px}
.scroll-down{left:902px;top:552px;width:62px;height:62px;border-radius:50%;background:var(--navy);border:3px solid #fff;display:flex;align-items:center;justify-content:center;z-index:3}

/* about */
.about-panel{left:0;top:649px;width:666px;height:505px;background:var(--navy)}
.about-photo{left:666px;top:583px;width:534px;height:571px;background:linear-gradient(150deg,#6e7f96 0%,#c9a58e 45%,#a97b62 60%,#d7dbe2 100%)}
.kicker-bar{width:4px;background:var(--accent)}
.kicker{font-size:16.5px;font-weight:500}
.sec-heading{font-size:28px;line-height:40px;font-weight:500}
.rule{height:1px}
.about-text{left:84px;top:934px;width:550px;font-size:13.6px;line-height:20px;color:#e8ebf0}

/* services */
.svc-label{left:0;width:1200px;top:1222px;text-align:center;font-size:16.5px;color:var(--ink)}
.svc-heading{left:100px;width:1000px;top:1259px;text-align:center;font-size:28px;line-height:40px;font-weight:400;color:var(--ink)}
.svc{top:1365px;width:310px;text-align:center}
.svc svg{display:block;margin:0 auto}
.svc h3{margin-top:22px;font-size:21.5px;line-height:30px;font-weight:600;color:var(--ink)}
.svc p{margin-top:12px;font-size:13.6px;line-height:20px;color:var(--body)}
.svc .more{display:block;margin-top:18px;font-size:13px;font-weight:600;color:var(--ink)}

/* why */
.why{left:0;top:1880px;width:1200px;height:665px;background:var(--muted)}
.why-pale{left:651px;top:2079px;width:549px;height:466px;background:var(--pale-blue)}
.why-text{left:90px;top:2262px;width:490px;font-size:13.6px;line-height:20px;color:var(--body)}
.card{background:var(--white);box-shadow:0 4px 16px rgba(20,30,50,.08);padding:16px 8px 0 16px;border-top:3px solid;overflow:hidden}
.card h4{font-size:19.5px;line-height:30px;font-weight:600;color:var(--ink)}
.card p{font-size:13.4px;line-height:20px;color:var(--body);margin-top:26px;max-height:100px;overflow:hidden;padding-right:6px}

/* contact + footer */
.footer-bg{left:0;top:2780px;width:1200px;height:527px}
.contact-card{left:117px;top:2580px;width:966px;height:323px;background:var(--white);border-radius:16px;box-shadow:0 6px 24px rgba(20,30,50,.08);text-align:center}
.contact-card h2{margin-top:70px;font-size:35px;font-weight:600;color:var(--brand-blue)}
.contact-card p{margin-top:16px;font-size:13.6px;line-height:20px;color:var(--brand-blue)}
.email-field{left:161px;top:207px;width:483px;height:49px;border:1px solid #cfd3da;border-radius:4px;font-size:16.5px;color:#9aa0a8;display:flex;align-items:center;padding-left:16px}
.submit{left:671px;top:207px;width:133px;height:49px;background:var(--brand-blue);color:#fff;border-radius:4px;font-weight:600;font-size:16.5px;display:flex;align-items:center;justify-content:center}
.f-brand{left:105px;top:2970px;color:#fff;font-size:21px;font-weight:500}
.f-about{left:105px;top:3010px;width:380px;color:#dfe3ea;font-size:13.6px;line-height:20px}
.f-head{top:2972px;color:#fff;font-size:16.5px;font-weight:500}
.f-link{color:#dfe3ea;font-size:13.6px}
.social{top:3009px;width:20px;height:20px;border-radius:50%;background:#3b7de0;border:2px solid #fff}
.copyright{left:119px;top:3264px;color:#dfe3ea;font-size:13px}
</style>
</head>
<body>

<header>
  <div class="abs hero" role="img" aria-label="Aerial photograph of a suburban roundabout surrounded by trees and houses"></div>
  <div class="abs hero-shade"></div>
  <div class="abs logo"><span class="logo-mark"></span>Tallowbrook</div>
  <nav>
    <span class="abs nav active" style="left:658px">HOME</span>
    <span class="abs nav" style="left:781px">ABOUT US</span>
    <span class="abs nav" style="left:928px">SERVICES</span>
    <span class="abs nav" style="left:1070px">CONTACT</span>
  </nav>
  <h1 class="abs hero-title">Innovating Property Management Excellence: Pioneering a Vision of Aspirational and Sustainable Communities</h1>
  <p class="abs hero-sub">At the forefront of the industry, our vision is to lead in delivering comprehensive property management services, showcasing our passion for innovation through cutting-edge technology.</p>
  <div class="abs hero-btn">READ MORE</div>
  <div class="abs scroll-down">
    <svg width="26" height="26" viewBox="0 0 26 26" fill="none" stroke="#fff" stroke-width="2.4" stroke-linecap="round" stroke-linejoin="round"><path d="M13 3v19M5 14l8 8 8-8"/></svg>
  </div>
</header>

<section class="about">
  <div class="abs about-panel"></div>
  <div class="abs about-photo" role="img" aria-label="Photograph of colleagues joining hands in a stacked grip over a desk"></div>
  <div class="abs kicker-bar" style="left:64px;top:728px;height:161px"></div>
  <div class="abs kicker" style="left:84px;top:730px;color:#fff">About Us</div>
  <h2 class="abs sec-heading" style="left:84px;top:768px;width:560px;color:#fff">Innovative Leadership in Property Management: Elevating Customer Trust Through Passion and Vision</h2>
  <div class="abs rule" style="left:64px;top:907px;width:580px;background:#3a4558"></div>
  <p class="abs about-text">At the heart of our company lies a commitment to instill unwavering trust in our customers, as they engage with our products and services, fostering a belief in our steadfast prioritization of their interests. We are a passionate entity, driven by a bold vision to lead the property management industry. Fearlessly embracing cutting-edge technology, we strive to enhance and innovate our offerings, embodying a visionary spirit that defines our organization's personality and sets us on a trajectory toward industry leadership</p>
</section>

<section class="services">
  <div class="abs svc-label">Our Services</div>
  <h2 class="abs svc-heading">Elevating Property Management Services: A Trust-Centric Approach with Innovative Solutions</h2>

  <svg width="0" height="0" style="position:absolute"><defs><linearGradient id="hexfill" x1="1" y1="0" x2="0" y2="1"><stop offset="0" stop-color="#1f9ccb"/><stop offset="1" stop-color="#176a8c"/></linearGradient></defs></svg>

  <div class="abs svc" style="left:108px">
    <svg width="146" height="167" viewBox="0 0 146 167"><polygon points="73,0 146,42 146,125 73,167 0,125 0,42" fill="url(#hexfill)"/>
      <g fill="none" stroke="#fff" stroke-width="2" stroke-linejoin="round" stroke-linecap="round"><path d="M58 84l15-13 15 13v16H58z"/><path d="M68 100v-8h10v8"/><path d="M48 92c0-14 10-24 25-24s25 10 25 24"/></g></svg>
    <h3>Trust-Centric Property Management</h3>
    <p>Our core service revolves around providing comprehensive and trust-centric property management solutions. From meticulous asset oversight to community engagement, we prioritize the interests of our clients, ensuring a transparent and reliable management experience that fosters lasting confidence.</p>
    <span class="more">Learn More ›</span>
  </div>

  <div class="abs svc" style="left:444px">
    <svg width="146" height="167" viewBox="0 0 146 167"><polygon points="73,0 146,42 146,125 73,167 0,125 0,42" fill="url(#hexfill)"/>
      <g fill="none" stroke="#fff" stroke-width="2" stroke-linejoin="round" stroke-linecap="round"><rect x="50" y="62" width="46" height="34" rx="2"/><path d="M73 96v10M62 106h22"/><path d="M62 84l11-10 11 10v8H62z"/></g></svg>
    <h3>Cutting-Edge Technological Integration</h3>
    <p>Our core service revolves around providing comprehensive and trust-centric property management solutions. From meticulous asset oversight to community engagement, we prioritize the interests of our clients, ensuring a transparent and reliable management experience that fosters lasting confidence.</p>
    <span class="more">Learn More ›</span>
  </div>

  <div class="abs svc" style="left:782px">
    <svg width="146" height="167" viewBox="0 0 146 167"><polygon points="73,0 146,42 146,125 73,167 0,125 0,42" fill="url(#hexfill)"/>
      <g fill="none" stroke="#fff" stroke-width="2" stroke-linejoin="round" stroke-linecap="round"><path d="M50 106h46"/><path d="M54 106V84l19-14 19 14v22"/><path d="M67 106V94h12v12"/><rect x="58" y="88" width="6" height="6"/><rect x="82" y="88" width="6" height="6"/><path d="M73 70v-8h8"/></g></svg>
    <h3>Customer-Centric Education and Support</h3>
    <p>Our core service revolves around providing comprehensive and trust-centric property management solutions. From meticulous asset oversight to community engagement, we prioritize the interests of our clients, ensuring a transparent and reliable management experience that fosters lasting confidence.</p>
    <span class="more">Learn More ›</span>
  </div>
</section>

<section class="why-section">
  <div class="abs why"></div>
  <div class="abs why-pale"></div>
  <div class="abs kicker-bar" style="left:68px;top:2061px;height:161px"></div>
  <div class="abs kicker" style="left:90px;top:2064px;color:var(--ink)">Why Customers Should Care ?</div>
  <h2 class="abs sec-heading" style="left:90px;top:2095px;width:490px;color:var(--ink)">Innovative Leadership in Property Management: Elevating Customer Trust Through Passion and Vision</h2>
  <div class="abs rule" style="left:68px;top:2234px;width:503px;background:var(--line)"></div>
  <p class="abs why-text">Our commitment to this innovative approach means that customers can expect not just a service, but an elevated experience that is both reliable and at the forefront of technological progress. By choosing our product, customers are investing in a management solution that prioritizes consistency, efficiency, and the ongoing pursuit of excellence</p>

  <div class="abs card" style="left:607px;top:1946px;width:244px;height:252px;border-color:#3a7bd5">
    <h4>Innovative Fusion of Technology and Rigorous Procedures</h4>
    <p style="margin-top:12px">Our product differentiation stems from a unique blend of cutting-edge technology and stringent procedures. Unlike competitors, we leverage adv...</p>
  </div>
  <div class="abs card" style="left:886px;top:1946px;width:244px;height:252px;border-color:var(--accent)">
    <h4>Consistency in Client Experience</h4>
    <p style="margin-top:44px">Unlike competitors who may lack a standardized approach, our commitment to rigorous procedures guarantees a consistently high level of servic...</p>
  </div>
  <div class="abs card" style="left:746px;top:2227px;width:245px;height:252px;border-color:#a87be6">
    <h4>Continuous Technological Advancements</h4>
    <p style="margin-top:12px">We stand out by continuously embracing and integrating the latest technological advancements in property management. This dedication...</p>
  </div>
</section>

<footer>
  <svg class="abs footer-bg" viewBox="0 0 1200 527" preserveAspectRatio="none"><path d="M0 10 C 300 -20, 700 30, 1200 80 L1200 527 L0 527 Z" fill="var(--navy-deep)"/></svg>

  <div class="abs contact-card">
    <h2>Get In Touch</h2>
    <p>Ready to embark on a transformative journey? Contact us today to explore how our<br>comprehensive consulting services can elevate your business to new heights.</p>
    <div class="abs email-field">Type your email address</div>
    <div class="abs submit">Submit</div>
  </div>

  <div class="abs f-brand">Tallowbrook</div>
  <p class="abs f-about">Lorem ipsum dolor sit amet consectetur. Sed aenean mauris volutpat in sollicitudin maecenas libero. Urna id lacus nec faucibus.</p>

  <div class="abs f-head" style="left:571px">Quick Links</div>
  <span class="abs f-link" style="left:571px;top:3009px">Home</span>
  <span class="abs f-link" style="left:571px;top:3049px">About</span>
  <span class="abs f-link" style="left:571px;top:3089px">Gallery</span>

  <div class="abs f-head" style="left:750px">Contact Us</div>
  <span class="abs f-link" style="left:750px;top:3009px">614.555.0182</span>
  <span class="abs f-link" style="left:750px;top:3049px">support@tallowbrookrm.com</span>

  <div class="abs f-head" style="left:986px">Follow Us</div>
  <span class="abs social" style="left:986px"></span>
  <span class="abs social" style="left:1026px"></span>
  <span class="abs social" style="left:1066px"></span>

  <div class="abs copyright">© 2023 Tallowbrook All Rights Reserved.</div>
</footer>

</body>
</html>
```